organic, healthy living website needs a new home page!

We need a home page for the front page of our website (www.fernmeadowco.com.au).

We want to see the following at a glance! We want to gain trust - communicate value, and navigate visitors to the next step - purchasing!

Our two main products:
- certified organic veggies (weekly in Melbourne, Australia - Mentone, Frankston and Ringwood with more pick up locations to come soon)

-ethical wooden toys (by membership only at this stage - run quarterly as a bulk buy - just for Melbourne people!)

Other products:
- health appliances - juicers, dehydrators and water filters (free delivery to their door all over Australia)

- natural parenting products which promote breastfeeding, homebirth, cosleeping and gentle parenting (books, jewellery, gifts, blessingway etc) all over Australia - send via Southern Parcelway.

This website holds all of our products for purchase. We want to emphasise exactly what is to offer here. We will have an info blog which we want to link THROUGH the product homepage of FM. The blog will include a directory of natural services (for a very niche market), recipes, stories, and a wealth of information to do with natural pregnancy, health, parenting, health and community!

We have 5 images linked below - we need these to correspond with the words PREGNANCY, BIRTH, PARENTING, HEALTH, And COMMUNITY and maybe a little design on these - such as dragonflies or flowers - or both. We will code these to work in a slideshow, and link to our blog.

We want this page to feature everything we do, but also be aesthetically pleasing without overkill. We want it to reflect our style, and vision. Natural, organic, and as close to nature as possible. Flow is important, as is consistency throughout the page. WE want it to appeal to our hippy mamas and papas who just want to love their babies, live organically and as healthy as they can.

We love the look and feel of the following websites:

http://brightlarderhub.com/

Thank you!!

Target Market(s)

20-50 year old parents who are environmentally aware and health conscious. They have very close bonds to their children.
Think bohemian, rustic, vintage yet with a modern feel.

Industry/Entity Type

Health

Font styles to use
Script

Colors
e34197
6b449b
33a6d7
0455a3
33b7a4

Requirements
Must have
• Must be clean and say at a glance exactly what we do.

```html
<!DOCTYPE html>
<html lang="en">
<head>
<meta charset="utf-8">
<title>Fern Meadow – Organic &amp; Natural Living</title>
<link href="https://fonts.googleapis.com/css2?family=Cinzel:wght@400;700&family=Lato:wght@400;700&display=swap" rel="stylesheet">
<style>
:root{
  --teal:#1d9bb2;
  --purple:#8a3a93;
  --purple-dark:#6b2f7a;
  --green:#6b9a3e;
  --green-dark:#4f7d2b;
  --blue-title:#2a86b0;
  --orange:#c9762b;
  --ink:#333;
  --muted:#777;
  --line:#cfcfcf;
  --footer:#eeeeee;
  --chat:#2f4a7f;
  --pink:#e34197;
  --indigo:#6b449b;
}
*{box-sizing:border-box;margin:0;padding:0}
html,body{width:799px;height:1200px;overflow:hidden;background:#fff}
body{position:relative;font-family:'Lato',sans-serif;color:var(--ink);font-size:8px}
.abs{position:absolute}

/* top */
.topbar{top:4px;right:152px;font-size:8px;color:#444;display:flex;gap:6px;align-items:center}
.topbar span+span{border-left:1px solid #999;padding-left:6px}
.brand{top:30px;left:158px;display:flex;align-items:center;gap:8px}
.brand-mark{width:30px;height:30px;border-radius:50%;background:var(--indigo)}
.brand-name{font-family:'Cinzel',serif;font-size:19px;color:var(--indigo)}
.search{top:38px;left:402px;width:242px;height:16px;display:flex}
.search input{flex:1;border:1px solid #ccc;background:#f2f2f2;font:8px 'Lato',sans-serif;padding-left:8px}
.search button{width:52px;background:var(--purple);color:#fff;border:0;font:700 8px 'Cinzel',serif;letter-spacing:.5px}
.cart{top:63px;right:155px;font-size:8px}
.cart b{font-family:'Cinzel',serif;color:var(--green);font-size:10px;margin-right:4px}
.dots{left:0;width:799px;border-top:1px dashed #aaa}
.nav{top:82px;left:155px;display:flex;gap:2px;height:17px}
.nav a{font:700 7px 'Lato',sans-serif;text-transform:uppercase;color:#444;text-decoration:none;padding:0 6px;line-height:17px}
.nav a.active{background:var(--teal);color:#fff}

/* features */
.feat-title{top:112px;width:240px;text-align:center;font:700 13px 'Cinzel',serif}
.feat-card{top:132px;width:238px;height:162px;border:1px solid #ccc;border-radius:12px;padding:6px;background:#fff}
.feat-photo{width:100%;height:148px;border-radius:8px}
.tag{position:absolute;bottom:-6px;left:50%;transform:translateX(-50%);background:var(--purple-dark);color:#fff;font-size:8px;padding:3px 12px;border-radius:3px;white-space:nowrap}
.members-seal{top:176px;left:364px;width:72px;height:72px;border-radius:50%;background:#fff;border:2px solid #ddd;display:flex;align-items:center;justify-content:center}
.members-seal i{width:26px;height:26px;border-radius:50%;background:var(--indigo)}
.shop-all{top:312px;width:200px;text-align:center;font:700 10px 'Cinzel',serif;border-bottom:1px dashed var(--purple);padding-bottom:4px}
.shop-all svg{vertical-align:middle;margin-left:4px}

/* products */
.carousel{top:342px;left:152px;width:494px;height:163px;border:1px solid #ddd;border-radius:4px}
.arrow{top:72px;color:#bbb;font-size:16px}
.products{position:absolute;left:22px;right:22px;top:8px;display:flex;justify-content:space-between}
.product{width:108px;text-align:center;font-size:7.5px;color:#555;white-space:nowrap}
.product .pic{height:90px;margin-bottom:8px;border-radius:4px}
.product .price{margin:3px 0 5px}
.product hr{border:0;border-top:1px dashed #bbb;margin-bottom:4px}

/* info */
.info{top:512px;width:244px;height:118px;border:1px solid #ddd;padding:6px 8px;overflow:hidden}
.info h3{position:relative;z-index:1;font:700 12px 'Cinzel',serif;color:var(--blue-title);white-space:nowrap}
.info h3 small{font:400 8px 'Lato',sans-serif;color:var(--blue-title)}
.info p{position:relative;z-index:1;font-size:7.5px;line-height:1.35;width:134px;margin-top:6px;color:#222;white-space:nowrap}
.info .art{position:absolute;right:0;top:24px;width:96px;height:94px}
.like{position:absolute;z-index:1;left:6px;bottom:6px;background:var(--chat);color:#fff;font-size:7px;padding:3px 8px 3px 4px;display:flex;gap:4px;align-items:center}
.like i{width:9px;height:9px;background:#fff}
.dot-green{display:inline-block;width:5px;height:5px;border-radius:50%;background:var(--teal)}

/* promos */
.promo{top:644px;height:82px;color:#fff;text-align:center;border:3px solid #fff;outline:1px solid #ddd;padding:8px}
.promo h4{font:700 12px 'Cinzel',serif;line-height:1.2}
.newsletter form{display:flex;margin:8px auto 5px;width:140px;height:15px}
.newsletter input{flex:1;border:0;font:7px 'Lato',sans-serif;padding-left:4px}
.newsletter button{width:38px;border:1px solid #fff;background:var(--purple-dark);color:#fff;font:700 7px 'Cinzel',serif}
.newsletter small{font:700 7px 'Cinzel',serif}
.quote p{font-size:7.5px;line-height:1.35;text-align:left;margin-top:4px}
.quote em{display:block;text-align:right;font-size:7px;font-weight:700}

/* blog */
.blog-title{top:746px;left:152px;width:494px;text-align:center;font:700 12px 'Cinzel',serif;color:var(--teal)}
.blog-title::before,.blog-title::after{content:"";position:absolute;top:8px;width:165px;border-top:1px dashed var(--teal)}
.blog-title::before{left:0}.blog-title::after{right:0}
.blog{top:769px;left:152px;width:494px;display:flex;gap:2px}
.post{flex:1;text-align:center}
.post h5{font:700 9px 'Cinzel',serif;color:#fff;text-align:left;padding:3px 5px;height:17px}
.post .pic{height:102px}
.post a{display:block;margin-top:8px;font-size:7.5px;color:#333;text-decoration:none;border-bottom:1px solid #ccc;padding-bottom:3px}

/* footer */
.footer{top:922px;left:0;width:799px;height:254px;background:var(--footer)}
.cols{position:absolute;top:10px;left:152px;width:494px;display:flex;justify-content:space-between}
.cols h6{font:700 7.5px 'Cinzel',serif;color:#333;margin-bottom:4px}
.cols li{list-style:none;font-size:7.5px;line-height:11px;color:#444}
.social{display:flex;gap:4px}
.social i{width:16px;height:16px;border-radius:50%;background:#8a8a8a}
.help{position:absolute;top:92px;left:0;width:799px;border-top:1px solid #ccc;border-bottom:1px solid #ccc;height:26px}
.help p{position:absolute;left:152px;top:8px;font:700 8px 'Cinzel',serif}
.help button{position:absolute;right:152px;top:4px;width:118px;height:17px;background:var(--purple-dark);color:#fff;border:0;font:700 8px 'Cinzel',serif}
.stats{position:absolute;left:152px;top:134px;font:400 12px 'Cinzel',serif;color:#555;line-height:15px}
.stats b{font-size:17px;letter-spacing:3px;color:#333;display:block;margin-top:3px}
.badge{position:absolute;top:140px;width:74px;height:74px;border-radius:50%}
.pay{position:absolute;left:514px;top:136px}
.pay h6{font:400 11px 'Cinzel',serif;color:#555;margin-bottom:6px}
.pay div{display:flex;align-items:center;gap:8px;font-size:7.5px;margin-bottom:6px}
.pay i{width:30px;height:13px;background:#fff;border:1px solid #ccc}
.copy{position:absolute;bottom:-24px;left:0;width:799px;height:24px;background:#dcdcdc;text-align:center;font-size:7.5px;line-height:24px;color:#333}
</style>
</head>
<body>

<div class="abs topbar"><span>&#9742; 555-014-2288</span><span>My account</span><span>Track order</span><span>Login</span></div>
<div class="abs brand"><i class="brand-mark"></i><span class="brand-name">Fern Meadow</span></div>
<form class="abs search"><input placeholder="Enter product name or code"><button type="button">SEARCH</button></form>
<div class="abs cart"><b>MY CART</b>2 Items - $40.00</div>
<div class="abs dots" style="top:78px"></div>
<nav class="abs nav">
  <a class="active">Home</a><a>Certified Organic Produce</a><a>Ethical Wooden Toys</a><a>Health Promotion</a><a>Natural Parenting</a><a>Register</a><a>Contact Us</a>
</nav>
<div class="abs dots" style="top:103px"></div>

<h2 class="abs feat-title" style="left:155px;color:var(--green)">Certified Organic Veggies</h2>
<h2 class="abs feat-title" style="left:403px;color:var(--orange)">Ethical Wooden Toys</h2>
<div class="abs feat-card" style="left:153px">
  <div class="feat-photo" role="img" aria-label="Photo of fresh organic vegetables and fruit" style="background:linear-gradient(135deg,#9fbe4a,#e07a2c 55%,#7c3f5e)"></div>
  <span class="tag">Open to everyone</span>
</div>
<div class="abs feat-card" style="left:405px">
  <div class="feat-photo" role="img" aria-label="Photo of a child's hand pushing a wooden toy car" style="background:linear-gradient(135deg,#d8c2a6,#b8875a 60%,#e6d8c6)"></div>
  <span class="tag">Members Only</span>
</div>
<div class="abs members-seal" role="img" aria-label="Melbourne members only seal"><i></i></div>
<div class="abs shop-all" style="left:172px">Shop all Vegetables &amp; Fruits<svg width="14" height="12" viewBox="0 0 14 12"><path d="M1 3h12l-2 8H3z" fill="var(--teal)"/></svg></div>
<div class="abs shop-all" style="left:428px">Shop all Ethical Wooden Toys<svg width="14" height="12" viewBox="0 0 14 12"><path d="M1 3h12l-2 8H3z" fill="var(--teal)"/></svg></div>

<section class="abs carousel">
  <span class="abs arrow" style="left:8px">&#8249;</span>
  <span class="abs arrow" style="right:8px">&#8250;</span>
  <div class="products">
    <div class="product"><div class="pic" role="img" aria-label="Red mommy bag with baby items" style="background:radial-gradient(circle,#d8353b 40%,#fff 72%)"></div>My First Mommy Bag<div class="price">$49.00</div><hr><svg width="10" height="9"><path d="M0 2h10l-2 7H2z" fill="var(--teal)"/></svg></div>
    <div class="product"><div class="pic" role="img" aria-label="Pack of Snugly medium size diapers" style="background:radial-gradient(circle,#3bb0a0 40%,#fff 72%)"></div>Snugly Medium Size Diapers<div class="price">$15.00</div><hr><svg width="10" height="9"><path d="M0 2h10l-2 7H2z" fill="var(--teal)"/></svg></div>
    <div class="product"><div class="pic" role="img" aria-label="Valley Herbals baby soap bar and box" style="background:radial-gradient(circle,#e8e2d6 40%,#fff 72%)"></div>Valley Herbals Baby Soap<div class="price">$10.00</div><hr><svg width="10" height="9"><path d="M0 2h10l-2 7H2z" fill="var(--teal)"/></svg></div>
    <div class="product"><div class="pic" role="img" aria-label="Colourful baby activity gym" style="background:radial-gradient(circle,#e6b43a 30%,#4a9bd0 50%,#fff 72%)"></div>Little Sprout Zoo Activity Gym<div class="price">$70.00</div><hr><svg width="10" height="9"><path d="M0 2h10l-2 7H2z" fill="var(--teal)"/></svg></div>
  </div>
</section>

<section class="abs info" style="left:152px">
  <h3>Fern Meadow</h3>
  <p>Baby Goods/Kids Goods<br>Natural pregnancy, birth<br>and parenting support, information<br>and products!<br>ORDERS: hello@fernmeadowco.com.au</p>
  <div class="art" role="img" aria-label="Illustration of overlapping family silhouettes" style="background:linear-gradient(120deg,#e77fb8,#3a6fc0 50%,#4fae5a)"></div>
  <span class="like"><i></i>Like Our Chatterbook Page</span>
</section>
<section class="abs info" style="left:402px">
  <h3>Fern Meadow <small>( melbourne members )</small></h3>
  <p>Health Food Store<br>Fruit &amp; Vegetable Store<br>Toy Store<br><span class="dot-green"></span> Always Open</p>
  <div class="art" role="img" aria-label="Illustration of a little house among green leaves" style="background:radial-gradient(circle at 60% 55%,#8fcf3a,#d9efb4 60%,#fff 80%)"></div>
  <span class="like"><i></i>Like Our Chatterbook Page</span>
</section>

<div class="abs promo" style="left:152px;width:160px;background:var(--teal)"><h4 style="margin-top:8px">Refer your friend &amp; get 10% off on your purchase</h4></div>
<div class="abs promo newsletter" style="left:319px;width:160px;background:var(--purple)"><h4>Join Free Newsletter</h4><form><input placeholder="Enter Email"><button type="button">JOIN</button></form><small>For Special Offers &amp; Promotions</small></div>
<div class="abs promo quote" style="left:486px;width:160px;background:var(--green)"><h4>They Loved Us</h4><p>&ldquo; Fern Produce is the best and most economical that I have found to buy from. The quality and freshness is great. Good variety and seasonal produce.</p><em>Mara Ellison (social)</em></div>

<h2 class="abs blog-title">&#9679; Our Blog Posts &#9679;</h2>
<section class="abs blog">
  <div class="post"><h5 style="background:var(--indigo)">Pregnancy</h5><div class="pic" role="img" aria-label="Photo of a pregnant belly" style="background:linear-gradient(#e8c9b4,#b58a72)"></div><a>Read now &rarr;</a></div>
  <div class="post"><h5 style="background:var(--pink)">Birth</h5><div class="pic" role="img" aria-label="Black and white photo of a mother with newborn" style="background:linear-gradient(#d8d8d8,#6e6e6e)"></div><a>Read now &rarr;</a></div>
  <div class="post"><h5 style="background:#e98a2c">Parenting</h5><div class="pic" role="img" aria-label="Photo of a family walking on the beach at sunset" style="background:linear-gradient(#f2c58a,#c8864a)"></div><a>Read now &rarr;</a></div>
  <div class="post"><h5 style="background:var(--green-dark)">Health</h5><div class="pic" role="img" aria-label="Photo of a basket of apples" style="background:linear-gradient(#9fc45a,#c0392b)"></div><a>Read now &rarr;</a></div>
  <div class="post"><h5 style="background:var(--blue-title)">Community</h5><div class="pic" role="img" aria-label="Photo of hands around a smiley shape in sand" style="background:linear-gradient(#e7ddc9,#c7a98a)"></div><a>Read now &rarr;</a></div>
</section>

<footer class="abs footer">
  <div class="cols">
    <ul><h6>Fern Meadow</h6><li>About Company</li><li>Privacy Policy</li><li>Why Us</li><li>Shipping Policy</li><li>Returns &amp; Exchange</li></ul>
    <ul><h6>Account</h6><li>Create Account</li><li>Manage Account</li><li>Change Password</li><li>Coupons &amp; Offers</li><li>My Shopping Bag</li></ul>
    <ul><h6>Shop</h6><li>Wooden Toys</li><li>Organic Veggies</li><li>Organic Fruits</li><li>Parenting</li><li>Health Appliances</li></ul>
    <ul><h6>Customer Care</h6><li>&#9742; 555-017-4410</li><li>Track Your Order</li><li>Email Us</li><li>Join Newsletter</li><li>Ask Our Expert</li></ul>
    <ul><h6>Connect Social</h6><div class="social"><i></i><i></i><i></i><i></i><i></i></div></ul>
  </div>
  <div class="help"><p>Need help? Contact Us &nbsp;/&nbsp; (or) Call us: +555-017-4410</p><button>BECOME MEMBER</button></div>
  <div class="stats">100+ Organic<br>2000+ Toys<br>100+ Natural Parenting<br>100+ Healthy Living<b>PRODUCTS</b></div>
  <div class="badge" role="img" aria-label="Fresh produce badge" style="left:322px;background:var(--green)"></div>
  <div class="badge" role="img" aria-label="Certified organic badge" style="left:410px;background:#4a5a2e;border:4px solid var(--green)"></div>
  <div class="pay"><h6>Payment Accepted</h6><div><i></i>Bank Deposit</div><div><i></i>PayWell</div></div>
  <div class="copy">&copy; 2004-2014 Fern Meadow, All Rights Reserved. &nbsp;/&nbsp; Terms &amp; Conditions | Read Our Privacy Policy</div>
</footer>
</body>
</html>
```